Website Design for NYC Female Attorney – Clean, Warm, Professional

Maren Holbeck, Esq.
www.MarenTHolbeckLegal.example

I’m a New York City-based attorney and CPA with a reputation for providing thoughtful, high-integrity legal guidance in both estate planning and small business law. I’ve served over 500 clients, and maintain a perfect 5-star rating. Clients come to me for clarity, compassion, and results — and I want my new website to reflect that.

**🎯 WHAT I NEED:**
A clean, modern, and emotionally resonant website that highlights who I am, what I do, and why clients trust me. It must feel approachable and warm, but still professional and elegant — think Quorvex meets boutique law firm. Feminine but not frilly.

**🧩 CORE WEBSITE SECTIONS (Top Navigation):**

1. **Home** – Strong first impression, tagline, CTA (book a call)
Homepage Copy (Sample Layout)
Headline:
Trusted Legal Guidance for Families and Founders.

Subheading:
Whether you’re protecting what you’ve built or building what’s next, I help you navigate estate planning and business law with confidence, compassion, and clarity.

Tagline (beneath logo or footer):
Legal Clarity for Life and Business.
2. **About Maren** – Bio, personal approach, credentials
3. **Services**

* *Estate Planning*
* *Business Law*
4. **Who I Work With** – Ideal clients (parents, entrepreneurs, etc.)
5. **Testimonials** – Client praise and social proof
6. **Success Stories** – Highlighting wins and case types
7. **FAQs** – Warm and clear answers to common questions
8. **Blog** – Thought leadership and helpful tips
8.5 Events
9. **Contact / Book a Call** – Scheduling or contact form

**🖼 STYLE DIRECTION:**

* Clean white backgrounds, soft jewel tones or neutrals
* Professional headshots and personal branding assets available
* Emphasis on readability, trust, and ease of navigation - THIS NEEDS TO BE BUILT OUT SO IT IS TRUSTED BY AI!
* No harsh colors, no corporate/legal clichés (e.g., gavels or scales) - I MEAN THIS. I DO NOT WANT A BORING LAW WEBSITE WITH SCALES AND GAVELS
* Feminine edge (not pink-heavy), with strong hierarchy and callouts

**💡 DESIGN NOTES:**

* Mobile-first design required
* Should include space for video or welcome message
* Easy to update blog or CMS area preferred
* Built in a user-friendly platform like WordPress, Webflow, or similar
* Needs to feel elevated enough to support high-end flat fee packages

**📣 TONE:**
Smart. Warm. Sophisticated. Human.

**⚖️ FINAL DELIVERABLES:**

* Homepage + 5+ interior pages
* Desktop + mobile views
* Style guide (fonts, colors, buttons)
* Bonus if you can help with copy layout/structure (not just visuals)

**📍TARGET AUDIENCE:**

* Busy professionals and families in NYC
* Women and couples who want peace of mind
* Entrepreneurs and creatives needing solid legal support

Here is my current site: www.MarenTHolbeckLegal.example
And here is a second business I have: www.QuickDayCounselDesk.example

Target Market(s)

Families and business owners

Industry/Entity Type

Law

Number of Pages Required

5+ page

Font styles to use
Serif
Sans Serif
Script

Requirements
Must have
• This website must be built to be seen as trustworthy by AI.

```html
<!DOCTYPE html>
<html lang="en">
<head>
<meta charset="utf-8">
<title>Maren Holbeck, Esq. – Law Office</title>
<link href="https://fonts.googleapis.com/css2?family=Poppins:wght@400;500;600;700&display=swap" rel="stylesheet">
<style>
:root{
  --bg:#f7f4ef;
  --navy:#2e3a5c;
  --navy-soft:#4a5a80;
  --mauve:#b58a93;
  --mauve-dark:#9b6f7a;
  --ink:#1e2230;
  --muted:#8a8c96;
  --line:#dcd9d3;
  --white:#ffffff;
  --star:#f2c21b;
  --photo:#5f7fa6;
}
*{box-sizing:border-box;margin:0;padding:0}
html,body{width:1200px;height:4570px;overflow:hidden}
body{background:var(--bg);font-family:"Poppins",sans-serif;color:var(--ink);position:relative}
.abs{position:absolute}
section,header,footer{position:absolute;left:0;width:1200px}
.btn{position:absolute;display:flex;align-items:center;justify-content:center;gap:8px;background:var(--navy-soft);color:var(--white);font-size:12px;font-weight:500;border-radius:4px}
.btn svg{width:9px;height:9px}
.btn.dark{background:var(--navy)}
.btn.mauve{background:var(--mauve)}
.photo{position:absolute;border-radius:22px}

/* header */
.site-header{top:0;height:110px}
.logo{left:66px;top:22px;width:126px;text-align:center;color:var(--navy)}
.logo small{display:block;font-size:10px;color:var(--mauve);letter-spacing:1px}
.logo strong{display:block;font-size:14px;font-weight:500;letter-spacing:1.5px;margin-top:14px}
.nav{left:296px;top:40px;display:flex;gap:0;font-size:11px;font-weight:500}
.nav a{color:var(--ink);text-decoration:none;padding:8px 16px;border-radius:3px;margin-right:22px}
.nav a.active{background:var(--navy);color:var(--white)}
.call{left:1015px;top:34px;width:124px;height:44px;font-size:13px}

/* hero */
.hero h1{position:absolute;left:56px;top:188px;font-size:34px;font-weight:500;line-height:50px;width:620px}
.hero .lead{position:absolute;left:56px;top:320px;font-size:16px;font-weight:500;line-height:26px;width:600px}
.stat{position:absolute;top:498px;font-size:13px;color:var(--muted)}
.stat b{display:block;color:var(--ink);font-size:16px;font-weight:500;margin-top:10px}

.trusted{top:680px;text-align:center;font-size:16px;color:var(--muted);line-height:26px}
.brand{position:absolute;top:750px;font-size:42px;font-weight:700;color:var(--navy)}

.about h2{position:absolute;left:594px;top:912px;font-size:26px;font-weight:500}
.about p{position:absolute;left:594px;top:990px;width:510px;font-size:13px;line-height:21px;color:var(--muted);text-align:justify}

/* services */
.band{background:var(--navy);color:var(--white)}
.services{top:1246px;height:730px}
.center-title{position:absolute;left:0;width:1200px;text-align:center;font-size:32px;font-weight:500}
.center-sub{position:absolute;left:0;width:1200px;text-align:center;font-size:16px;font-weight:500}
.svc{position:absolute;top:135px;width:406px;height:196px;border-radius:6px;padding:34px 22px;background:linear-gradient(110deg,#4b4e6e 0%,#9a7a8a 70%,#c09aa2 100%)}
.svc.rev{background:linear-gradient(110deg,#b08d98 0%,#7a6a85 55%,#4a4f70 100%)}
.svc .num{font-size:28px}
.svc h3{font-size:17px;font-weight:400;margin-top:20px}
.svc p{font-size:12px;line-height:18px;margin-top:12px}
.clients h2{position:absolute;left:110px;top:500px;font-size:32px;font-weight:600;line-height:50px}
.clients p{position:absolute;left:110px;top:612px;width:220px;font-size:13px;line-height:21px}
.who{position:absolute;top:476px;width:170px;height:196px;background:var(--white);color:var(--ink);border-radius:3px;padding:12px 8px}
.who.on{background:var(--mauve);color:var(--white)}
.who svg{width:22px;height:22px}
.who small{position:absolute;left:8px;top:112px;width:150px;font-size:10px;line-height:15px}
.who hr{position:absolute;left:8px;right:8px;top:150px;border:0;border-top:1px solid currentColor;opacity:.5}
.who b{position:absolute;left:8px;top:160px;font-size:14px;font-weight:500}

/* testimonials */
.testi{top:1976px;height:618px;color:var(--ink)}
.tcard{position:absolute;top:230px;width:234px;height:254px;background:var(--white);border-radius:4px;text-align:center;padding-top:54px}
.avatar{position:absolute;top:-58px;left:62px;width:110px;height:110px;border-radius:50%;border:4px solid var(--white);background:radial-gradient(circle at 50% 40%,#b89a86,#5a4a40)}
.stars{color:var(--star);font-size:19px;letter-spacing:5px}
.tcard h4{font-size:13px;font-weight:600;margin-top:12px}
.tcard p{font-size:9px;color:var(--muted);line-height:13px;text-align:left;padding:0 30px;margin-top:26px}
.tcard .who-name{position:absolute;left:30px;top:210px;text-align:left;font-size:8px;line-height:12px;color:var(--ink)}
.tcard .who-name span{color:var(--muted)}
.arrow{position:absolute;top:312px;width:32px;height:32px;border-radius:50%;background:var(--navy);display:flex;align-items:center;justify-content:center}

/* success */
.success{top:2594px;height:542px}
.story{position:absolute;top:133px;width:292px;background:var(--white);border-radius:3px;padding:8px;color:var(--ink)}
.story .img{height:184px;border-radius:2px;position:relative}
.tag{position:absolute;left:6px;top:8px;background:var(--white);font-size:10px;padding:4px 8px;border-radius:3px}
.story h4{font-size:12px;font-weight:600;line-height:18px;margin:14px 8px 0}
.story p{font-size:9px;color:var(--muted);line-height:15px;margin:6px 8px 0}
.story .btn{position:static;width:102px;height:36px;margin:14px 8px 6px auto;font-size:11px}

/* faq */
.faq{top:3136px;height:780px}
.q{position:absolute;left:82px;width:1036px;border:2px solid var(--line);border-radius:8px;background:var(--white);padding:0 22px;font-size:16px;font-weight:500}
.q .row{display:flex;justify-content:space-between;align-items:center;height:64px}
.q .ans{font-size:13px;font-weight:400;color:#55585f;border-top:1px solid var(--line);padding-top:14px}
.q .sign{font-size:22px;font-weight:400}

/* contact */
.contact{top:3916px;height:340px}
.contact h2{position:absolute;left:102px;font-size:24px;font-weight:500}
.contact h3{position:absolute;font-size:20px;font-weight:500}
.contact .small{position:absolute;font-size:12px;color:var(--muted)}
.contact .val{position:absolute;font-size:14px;font-weight:500}
.field{position:absolute;border:1px solid var(--line);background:var(--white);border-radius:3px;font-size:12px;color:var(--muted);padding:8px 10px}

/* footer */
.site-footer{top:4260px;height:310px}
.flogo{position:absolute;left:140px;top:90px;width:256px;text-align:center;color:var(--navy)}
.flogo small{display:block;font-size:18px;color:var(--navy);letter-spacing:3px}
.flogo strong{display:block;font-size:30px;font-weight:500;letter-spacing:2px;margin-top:40px}
.flinks{position:absolute;top:92px;font-size:13px;color:var(--muted);line-height:27px}
.fcol{position:absolute;left:895px;font-size:13px;line-height:21px}
.fcol span{display:block;color:var(--muted)}
.social{position:absolute;top:224px;width:34px;height:34px;border-radius:50%;background:var(--mauve)}
.copy{position:absolute;left:0;width:1200px;top:294px;text-align:center;font-size:10px}
</style>
</head>
<body>

<header class="site-header">
  <div class="abs logo"><small>LAW OFFICE OF</small><strong>MAREN HOLBECK</strong></div>
  <nav class="abs nav">
    <a class="active">Home</a><a>About</a><a>Services ⌄</a><a>Testimonials</a><a>Blog</a><a>FAQs</a><a>Contact</a>
  </nav>
  <div class="btn dark call">Book a Call
    <svg viewBox="0 0 24 24" style="width:13px;height:13px"><path fill="#fff" d="M6.6 10.8a15 15 0 006.6 6.6l2.2-2.2c.3-.3.7-.4 1-.2 1.1.4 2.3.6 3.6.6.6 0 1 .4 1 1V20c0 .6-.4 1-1 1A17 17 0 013 4c0-.6.4-1 1-1h3.5c.6 0 1 .4 1 1 0 1.3.2 2.5.6 3.6.1.3 0 .7-.2 1z"/></svg>
  </div>
</header>

<section class="hero" style="top:0;height:640px">
  <h1>Trusted Legal Guidance for Families and Founders.</h1>
  <p class="lead">I help you navigate estate planning and business law with confidence, compassion, and clarity.</p>
  <div class="btn" style="left:56px;top:406px;width:184px;height:44px;font-size:13px">Schedule a Free Call <svg viewBox="0 0 10 10"><path d="M2 8L8 2M3 2h5v5" stroke="#fff" stroke-width="1.3" fill="none"/></svg></div>
  <div class="stat" style="left:66px">Years Practicing<b>10+ Years</b></div>
  <div class="abs" style="left:215px;top:498px;width:1px;height:50px;background:var(--line)"></div>
  <div class="stat" style="left:250px">Clients Served<b>500+ Satisfied Clients</b></div>
  <div class="photo" style="left:745px;top:130px;width:400px;height:470px;background:var(--mauve);border-radius:30px"></div>
  <div class="photo" role="img" aria-label="Portrait of the attorney seated in a dark dress" style="left:728px;top:146px;width:400px;height:470px;border-radius:30px;background:linear-gradient(160deg,#6b8db5,#4d6d95)"></div>
</section>

<section class="trusted" style="top:680px;height:160px">
  <div>Trusted By Clients Across Platforms</div>
  <div>5-Star Ratings On</div>
</section>
<div class="brand" style="left:250px">Revuly</div>
<div class="brand" style="left:510px">Counselry</div>
<div class="brand" style="left:796px">Starvane</div>

<section class="about" style="top:0;height:1246px">
  <div class="photo" role="img" aria-label="Headshot of the attorney against a blue backdrop" style="left:126px;top:884px;width:382px;height:292px;background:linear-gradient(160deg,#6f90b6,#4e6e96)"></div>
  <h2>ABOUT MAREN</h2>
  <p>Hi, I'm Maren — A New York City Attorney And CPA. I Combine Legal Strategy With Human Insight To Help My Clients Protect What Matters Most. With Over 500 Satisfied Clients And A 5-Star Reputation, My Mission Is Simple To Bring Clarity And Peace To Your Legal Journey.</p>
  <div class="btn dark" style="left:594px;top:1115px;width:104px;height:36px;font-size:11px">Learn More <svg viewBox="0 0 10 10"><path d="M2 8L8 2M3 2h5v5" stroke="#fff" stroke-width="1.3" fill="none"/></svg></div>
</section>

<section class="band services">
  <div class="center-title" style="top:36px">SERVICES</div>
  <div class="center-sub" style="top:82px">Bringing You Cutting-Edge Legal Solutions Tailored To Your Unique Needs.</div>
  <div class="svc" style="left:168px"><div class="num">01</div><h3>Inheritance Planning</h3><p>Protect Your Family And Ensure Your Wishes Are Carried Out With Clear And Empathetic Estate Planning.</p></div>
  <div class="svc rev" style="left:626px"><div class="num">02</div><h3>Business Law</h3><p>Smart Legal Guidance For Startups, Entrepreneurs, And Growing Businesses — From Setup To Scaling.</p></div>
  <div class="btn mauve" style="left:548px;top:360px;width:104px;height:36px;font-size:11px">Learn More <svg viewBox="0 0 10 10"><path d="M2 8L8 2M3 2h5v5" stroke="#fff" stroke-width="1.3" fill="none"/></svg></div>
  <div class="clients">
    <h2>CLIENTS I<br>WORK WITH</h2>
    <p>Is This You? You're In The Right Place.</p>
    <div class="who on" style="left:362px"><svg viewBox="0 0 24 24"><circle cx="8" cy="7" r="3" fill="#2e3a5c"/><circle cx="16" cy="7" r="3" fill="#2e3a5c"/><path d="M2 20l6-9 6 9M10 20l6-9 6 9" stroke="#2e3a5c" stroke-width="2" fill="none"/></svg><small>Peace Of Mind For Their Children.</small><hr><b>Parents</b></div>
    <div class="who" style="left:548px"><svg viewBox="0 0 24 24"><circle cx="12" cy="9" r="5" fill="var(--mauve)"/><rect x="10" y="14" width="4" height="5" fill="var(--mauve)"/></svg><small>Building Something Meaningful.</small><hr><b>Entrepreneurs</b></div>
    <div class="who" style="left:734px"><svg viewBox="0 0 24 24"><rect x="3" y="8" width="18" height="12" rx="2" fill="var(--mauve)"/><rect x="9" y="4" width="6" height="4" fill="none" stroke="var(--mauve)" stroke-width="2"/></svg><small>Managing Business + Personal Assets.</small><hr><b>Professionals</b></div>
    <div class="who" style="left:920px"><svg viewBox="0 0 24 24"><path d="M4 4v16h16" stroke="var(--mauve)" stroke-width="2" fill="none"/><path d="M8 16l10-10" stroke="var(--mauve)" stroke-width="2"/></svg><small>Contracts That Actually Make Sense.</small><hr><b>Creatives</b></div>
  </div>
</section>

<section class="testi">
  <div class="center-title" style="top:76px;font-size:26px">TESTIMONIALS</div>
  <div class="center-sub" style="top:118px;font-size:13px">What Clients Are Saying ?</div>
  <div class="arrow" style="left:169px"><svg width="14" height="14" viewBox="0 0 14 14"><path d="M12 7H2M6 3L2 7l4 4" stroke="#fff" stroke-width="1.5" fill="none"/></svg></div>
  <div class="arrow" style="left:999px"><svg width="14" height="14" viewBox="0 0 14 14"><path d="M2 7h10M8 3l4 4-4 4" stroke="#fff" stroke-width="1.5" fill="none"/></svg></div>
  <div class="tcard" style="left:238px"><div class="avatar" role="img" aria-label="Client portrait"></div><div class="stars">★★★★★</div><h4>Kind, clear, and trustworthy.</h4><p>Maren didn't just give legal advice — she truly listened and made me feel safe throughout the process.</p><div class="who-name">Tessa R.<br><span>Creative Director</span></div></div>
  <div class="tcard" style="left:483px"><div class="avatar" role="img" aria-label="Client portrait"></div><div class="stars">★★★★★</div><h4>Exactly what I needed</h4><p>Clear answers, no pressure, and real human connection. That's rare — but Maren delivered it.</p><div class="who-name">Noor B.<br><span>Creative Director</span></div></div>
  <div class="tcard" style="left:728px"><div class="avatar" role="img" aria-label="Client portrait"></div><div class="stars">★★★★★</div><h4>Professional and personal.</h4><p>It felt less like hiring a lawyer, and more like working with a trusted guide.</p><div class="who-name">Ilan V.<br><span>Marketing Strategist</span></div></div>
  <div class="btn dark" style="left:550px;top:512px;width:100px;height:36px;font-size:11px">Read More <svg viewBox="0 0 10 10"><path d="M2 8L8 2M3 2h5v5" stroke="#fff" stroke-width="1.3" fill="none"/></svg></div>
</section>

<section class="band success">
  <div class="center-title" style="top:40px;font-size:28px">SUCCESS STORIES</div>
  <div class="center-sub" style="top:82px;font-size:13px">Real Clients. Real Impact.</div>
  <div class="story" style="left:108px"><div class="img" role="img" aria-label="Hands reviewing documents at a table" style="background:linear-gradient(135deg,#c9c6c0,#8f8c86)"><span class="tag">Inheritance Planning</span></div><h4>Ibu Rhea's Family: Realizing Last Wishes With Complete Peace Of Mind.</h4><div class="btn">Read More <svg viewBox="0 0 10 10"><path d="M2 8L8 2M3 2h5v5" stroke="#fff" stroke-width="1.3" fill="none"/></svg></div></div>
  <div class="story" style="left:455px"><div class="img" role="img" aria-label="Person signing a contract on a desk" style="background:linear-gradient(135deg,#e8e6e2,#c89a6a)"><span class="tag">Business Law</span></div><h4>The Creator's Vision : Protecting Startup Innovation 'XYZ Labs' From The Start.</h4><p>From A Brilliant Idea To A Strong Legal Entity, We Assisted The Founders Of 'XYZ Labs' Secure Their Crucial Intellectual Property And Contracts.</p><div class="btn">Read More <svg viewBox="0 0 10 10"><path d="M2 8L8 2M3 2h5v5" stroke="#fff" stroke-width="1.3" fill="none"/></svg></div></div>
  <div class="story" style="left:800px"><div class="img" role="img" aria-label="Professional woman seated at an office desk" style="background:linear-gradient(135deg,#7c8ea6,#2b3140)"><span class="tag">Dual Needs</span></div><h4>Holistic Solutions : Overcoming Mr. Devran's Personal And Business Legal Challenges</h4><div class="btn">Read More <svg viewBox="0 0 10 10"><path d="M2 8L8 2M3 2h5v5" stroke="#fff" stroke-width="1.3" fill="none"/></svg></div></div>
</section>

<section class="faq">
  <div class="center-title" style="top:78px;font-size:28px">FAQ'S</div>
  <div class="center-sub" style="top:138px;font-size:16px">You've Got Questions. I've Got Straight Answers.</div>
  <div class="q" style="top:192px;height:114px"><div class="row">What's The First Step If I Want To Work With You ?<span class="sign">−</span></div><div class="ans">Easy — Just Book A Free Consultation. We'll Talk Through Your Needs And Decide If We're A Good Fit. No Pressure, No Jargon.</div></div>
  <div class="q" style="top:322px;height:68px"><div class="row">Do You Offer Flat Fees Or Hourly Rates?<span class="sign">+</span></div></div>
  <div class="q" style="top:409px;height:68px"><div class="row">I've Never Worked With A Lawyer. Will I Understand Everything?<span class="sign">+</span></div></div>
  <div class="q" style="top:496px;height:68px"><div class="row">What Makes You Different From Other Attorneys?<span class="sign">+</span></div></div>
  <div class="q" style="top:583px;height:68px"><div class="row">Do You Only Work With Clients In NYC?<span class="sign">+</span></div></div>
  <div class="center-sub" style="top:680px;font-size:16px">Still Have Questions?</div>
  <div class="btn dark" style="left:548px;top:732px;width:104px;height:36px;font-size:11px">Book A Call <svg viewBox="0 0 10 10"><path d="M2 8L8 2M3 2h5v5" stroke="#fff" stroke-width="1.3" fill="none"/></svg></div>
</section>

<section class="contact">
  <h2 style="top:86px">Contact Us</h2>
  <p class="small" style="left:102px;top:124px;width:460px;line-height:21px;text-align:justify">We Are Always Ready To Listen And Provide The Legal Guidance You Need. Feel Free To Contact Our Team For Questions, Clarifications, Or To Start A Discussion About Your Specific Needs.</p>
  <h3 style="left:102px;top:212px">Chat To Us</h3>
  <span class="small" style="left:102px;top:248px">email</span>
  <span class="val" style="left:102px;top:266px">hello@marenholbecklegal.example</span>
  <h3 style="left:396px;top:212px">Call Us</h3>
  <span class="small" style="left:396px;top:248px">phone</span>
  <span class="val" style="left:396px;top:266px">(212) 555-0147</span>
  <div class="field" style="left:693px;top:60px;width:182px;height:36px">First Name</div>
  <div class="field" style="left:888px;top:60px;width:210px;height:36px">Last Name</div>
  <div class="field" style="left:693px;top:112px;width:405px;height:36px">Email</div>
  <div class="field" style="left:693px;top:164px;width:405px;height:76px">Message</div>
  <div class="btn dark" style="left:693px;top:256px;width:405px;height:42px;font-size:13px">Send Message</div>
</section>

<footer class="site-footer">
  <div class="flogo"><small>LAW OFFICE OF</small><strong>MAREN HOLBECK</strong></div>
  <div class="flinks" style="left:600px">Home<br>About<br>Services</div>
  <div class="flinks" style="left:725px">Testimonials<br>FAQs<br>Contact</div>
  <div class="fcol" style="top:94px"><span>address</span>48 Lindell Row, Fl 9<br>New York, NY 10099</div>
  <div class="fcol" style="top:176px"><span>phone</span>(212) 555-0147</div>
  <div class="fcol" style="top:236px"><span>email</span>hello@marenholbecklegal.example</div>
  <div class="social" style="left:600px"></div>
  <div class="social" style="left:659px"></div>
  <div class="social" style="left:717px"></div>
  <div class="social" style="left:776px"></div>
  <div class="copy">© 2025 Maren Holbeck Law PLLC. All Rights Reserved.</div>
</footer>

</body>
</html>
```